Flyer für einen Hersteller von Campingzubehör
Zielgruppe
Wir sind Hersteller von Campingzubehör, in der Hauptsache für Wohnmobile und Markisen. Zielgruppe sind daher alle Camper mit entsprechenden Freizeitfahrzeugen. Bei diesem Flyer soll der Camper aufmerksam werden, das der Sonnenschutz individuell bedruckt werden kann, mit eigenen Motiven. Viele lasse sich auf das Sonnensegel eine schöne Urlaubserinnerung, den Hund, oder etwas was dem Camper lieb und wichtig ist. Eben ganz individuell. Wichtig ist das der Sonnenschutz Made in Germany ist! und absolut werkzeugfrei handzuhaben ist. Spezifikationen werden von uns eingefügt.
Aufgabenstellung
Der Flyer soll nach der beiliegenden Druckvorlage erstellt werden. Falzflyer, DIN A5, 4 Seiten. Sinngemäße Angabe in der Vorlage. Auf der 4 Seite soll das Bestellformular erscheinen, also diese Seite bitte freilassen und 'nur' die 3 Seiten gestalten.
Auf der Titelseite soll das auf das 'Schattenproblem' aufmerksam gemacht werden. Ich bin sehr gespannt! Bei Fragen bitte melden. Für den Hintergrund lasse ich dem Designer feien lauf...

```html
<!DOCTYPE html>
<html lang="de">
<head>
<meta charset="utf-8">
<title>Falzflyer Sonnenschutz</title>
<link href="https://fonts.googleapis.com/css2?family=Montserrat:wght@400;500;600;700;800&family=Open+Sans:ital,wght@0,400;0,600;1,400&display=swap" rel="stylesheet">
<style>
  :root{
    --bg:#efefef;
    --green-dark:#66a840;
    --green:#8cc63f;
    --green-light:#9ccf4a;
    --ink:#1f1f1f;
    --white:#ffffff;
    --paper-gray:#ececec;
  }
  *{box-sizing:border-box;margin:0;padding:0}
  html,body{width:857px;height:1200px;overflow:hidden;background:var(--bg)}
  body{position:relative;font-family:"Open Sans",sans-serif;color:var(--ink)}
  .spread{position:absolute;left:48px;width:760px;height:537px;display:flex;box-shadow:0 6px 18px rgba(0,0,0,.12)}
  .spread--outside{top:40px}
  .spread--inside{top:617px}
  .page{position:relative;width:380px;height:537px;overflow:hidden}

  /* outside */
  .page--back{background:var(--green-dark)}
  .page--cover{background:var(--green-light)}
  .cover-photo{position:absolute;left:0;top:0;width:380px;height:300px;
    background:linear-gradient(180deg,#4a8fd6 0%,#8fc0ea 35%,#4f8fa6 55%,#7a8f6a 75%,#9a9478 100%)}
  .brand{position:absolute;right:18px;top:62px;width:126px;height:66px;background:var(--white);
    display:flex;align-items:center;justify-content:center;gap:6px;padding:0 8px}
  .brand-dot{width:10px;height:10px;border-radius:50%;background:var(--green);flex:none}
  .brand-name{font-family:"Montserrat",sans-serif;font-weight:700;font-size:11px;line-height:1.15;color:var(--green)}
  .cover-inset{position:absolute;left:40px;top:246px;width:270px;height:128px;
    background:linear-gradient(90deg,#e38a2a 0%,#3b3a52 45%,#e9ecee 70%,#d9dcde 100%)}
  .cover-title{position:absolute;left:28px;top:400px;font-family:"Montserrat",sans-serif;
    font-weight:800;font-size:29px;color:var(--white);letter-spacing:.5px;white-space:nowrap}
  .cover-sub{position:absolute;left:28px;top:440px;font-family:"Montserrat",sans-serif;
    font-weight:500;font-size:17px;color:var(--white);letter-spacing:.6px;white-space:nowrap}

  /* inside left */
  .page--features{background:var(--paper-gray)}
  .hero-photo{position:absolute;left:0;top:0;width:380px;height:240px;
    background:linear-gradient(180deg,#9cc98a 0%,#6fae3c 55%,#4f9a26 100%)}
  .motif-panel{position:absolute;left:58px;top:40px;width:190px;height:138px;background:#111;
    display:flex;align-items:center;justify-content:center;text-align:center;
    font-family:"Montserrat",sans-serif;font-weight:500;font-size:15px;line-height:1.25;color:var(--white)}
  .thumb{position:absolute;top:252px;width:178px;height:112px}
  .thumb--one{left:10px;background:linear-gradient(135deg,#c9a98a,#b77fc4 45%,#7bb94a)}
  .thumb--two{left:192px;background:linear-gradient(180deg,#4f86d6,#a5c9ee 50%,#5aa32e)}
  .checklist{position:absolute;top:384px;list-style:none;font-family:"Montserrat",sans-serif;
    font-weight:600;font-size:13.5px;line-height:25px}
  .checklist--left{left:26px}
  .checklist--right{left:210px}
  .checklist li{display:flex;align-items:center;gap:9px}
  .tick{width:15px;height:12px;flex:none}
  .bottom-band{position:absolute;left:0;bottom:0;width:380px;height:14px;background:var(--green)}

  /* inside right */
  .page--details{background:var(--white);padding:34px 30px 0 30px}
  .details-title{font-family:"Montserrat",sans-serif;font-weight:700;font-size:19px;line-height:1.1;color:var(--green);letter-spacing:.3px}
  .title-rule{width:48px;height:2px;background:var(--green);margin:10px 0 14px}
  .details-body{font-size:8.2px;line-height:1.5;color:var(--ink);margin-bottom:9px}
  .price{font-family:"Montserrat",sans-serif;font-weight:700;font-style:italic;font-size:22px;color:var(--green);margin-top:10px}
  .price-note{font-size:7.5px;margin-top:2px}
  .shipping{font-size:6.8px;font-style:italic;line-height:1.4;color:var(--green);margin-top:10px;width:150px}
  .origin-mark{position:absolute;right:40px;bottom:40px;width:70px;height:30px;display:flex;flex-direction:column;border-radius:3px;overflow:hidden}
  .origin-mark span{flex:1}
  .origin-mark .s1{background:#111}.origin-mark .s2{background:#d62718}.origin-mark .s3{background:#f2c21b}
  .page-edge{position:absolute;left:0;bottom:0;width:380px;height:8px;background:var(--green)}
</style>
</head>
<body>

<section class="spread spread--outside">
  <div class="page page--back"></div>
  <div class="page page--cover">
    <div class="cover-photo" role="img" aria-label="Wohnmobil mit Markise und E-Bikes an einem Bergsee unter blauem Himmel"></div>
    <div class="brand">
      <span class="brand-dot"></span>
      <span class="brand-name">Wegzeit<br>Campingteile</span>
    </div>
    <div class="cover-inset" role="img" aria-label="Wohnmobil mit bedrucktem Sonnensegel, Motiv Sonnenuntergang am See"></div>
    <h1 class="cover-title">WIEDER LIEFERBAR!</h1>
    <p class="cover-sub">Drucken Sie Ihr eigenes Motiv</p>
  </div>
</section>

<section class="spread spread--inside">
  <div class="page page--features">
    <div class="hero-photo" role="img" aria-label="Wohnmobil auf grüner Wiese mit ausgefahrener Markise und Sonnensegel"></div>
    <div class="motif-panel">Drucken Sie<br>hier Ihr<br>eigenes Motiv</div>
    <div class="thumb thumb--one" role="img" aria-label="Wohnmobil mit Sonnensegel, bedruckt mit einem Hundemotiv"></div>
    <div class="thumb thumb--two" role="img" aria-label="Wohnmobil mit Sonnensegel, bedruckt mit einer Landschaft"></div>
    <ul class="checklist checklist--left">
      <li><svg class="tick" viewBox="0 0 15 12"><path d="M1 6 L5.5 10.5 L14 1.5" fill="none" stroke="#8cc63f" stroke-width="2.4"/></svg>Sonnenschutz</li>
      <li><svg class="tick" viewBox="0 0 15 12"><path d="M1 6 L5.5 10.5 L14 1.5" fill="none" stroke="#8cc63f" stroke-width="2.4"/></svg>Sichtschutz</li>
      <li><svg class="tick" viewBox="0 0 15 12"><path d="M1 6 L5.5 10.5 L14 1.5" fill="none" stroke="#8cc63f" stroke-width="2.4"/></svg>Regenschutz</li>
    </ul>
    <ul class="checklist checklist--right">
      <li><svg class="tick" viewBox="0 0 15 12"><path d="M1 6 L5.5 10.5 L14 1.5" fill="none" stroke="#8cc63f" stroke-width="2.4"/></svg>UV Beständig</li>
      <li><svg class="tick" viewBox="0 0 15 12"><path d="M1 6 L5.5 10.5 L14 1.5" fill="none" stroke="#8cc63f" stroke-width="2.4"/></svg>280gqm</li>
      <li><svg class="tick" viewBox="0 0 15 12"><path d="M1 6 L5.5 10.5 L14 1.5" fill="none" stroke="#8cc63f" stroke-width="2.4"/></svg>mit Ösen</li>
    </ul>
    <div class="bottom-band"></div>
  </div>

  <div class="page page--details">
    <h2 class="details-title">LICHTWEHR 3M X 2,2M<br>LIEFERBAR!</h2>
    <div class="title-rule"></div>
    <p class="details-body">Transparentes Meshewebe, das Licht und Luft durchlässt, aber Wärme blockiert. Höhe 2,20m und 3m breit. Passt in jede Kederleiste von Nordrand, Schattline oder Solvento! Das Meshgewebe ist wasserfest und hält bis zu 96% der UV Strahlung ab. Nässe ist kein Problem, das Sonnensegel wird kurz geschüttelt und ist sofort trocken! Ein weiterer Nutzen ist, man sieht nicht wer oder ob hinter dem Sonnensegel jemand sitzt, aber man sieht jeden der vorbei geht! Ein Stück mehr Privatsphäre am Campingplatz.</p>
    <p class="details-body">Das Sonnensegel wird einfach in die vorhandene Kederleiste der Markise eingezogen und Sie genießen den Schatten. Das untere Ende ist aus PVC und mit 3 Ösen versehen, damit das Segel abgespannt werden kann. Heringe und Befestigungsmaterial sind selbstverständlich dabei. Auch die Tasche ist im Lieferumfang enthalten.</p>
    <p class="price">129,00 €</p>
    <p class="price-note">inkl. MwSt. versandkostenfrei in bestimmte Länder</p>
    <p class="shipping">Versandkostenfrei in folgende Länder: Albanien, Andorra, Belarus, Belgien, Bosnien und Herzegowina, Bulgarien, Deutschland, Serbien und Montenegro, Tschechische Republik, Zypern Mehr anzeigen</p>
    <div class="origin-mark" aria-hidden="true"><span class="s1"></span><span class="s2"></span><span class="s3"></span></div>
    <div class="page-edge"></div>
  </div>
</section>

</body>
</html>
```